I need a logo design for a new company based in Tucson called "Mindtrainer Lou Varga". I am a psychotherapist that specializes in clinical psychology with athletes and performers. The final design should incorporate the psychology symbol as a watermark. The logo should convey movement and fluidity. "Mindtrainer" is a bit of a play on words combining psychology (head) with sports (coach). Other design interests include mid-century, Gustav Orrin Pell. I will want to use the logo for business cards, letterhead and marketing brochures. I will put together a website at a later date. I am attaching a file with some pertinent information for the business card. Thank you.
Lou Varga
mindtrainerlouvarga@quellmail.net
Updates

Thank you all for the submissions so far.  I have submitted an additional file with a draft of a new design idea.  Since "mindtrainer" is a bit of a play on words, I would like to see something with the two "H's" look something like quotation marks.  If the psychology logo is to be included at all, it needs to be less prominent.     Thank you all.  Lou                               

Target Market(s)

1) Adolescent and adult athletes and performers who are looking to increase their level of performance (Sport and Performance Psychology)
2) Adult psychotherapy patients (Clinical psychology)

Industry/Entity Type

Marketing

Colors

Designer to choose colors to be used in the design.

Requirements
Must have
• 1) Since "mindtrainer" is a bit of a play on words, The "H's" need to be in a font that looks somewhat like quotation marks.

Nice to have
• Logo on one side. All other info on the backside?

```html
<!DOCTYPE html>
<html lang="en">
<head>
<meta charset="utf-8">
<title>Mindtrainer Lou Varga – Business Card</title>
<link rel="stylesheet" href="https://fonts.googleapis.com/css2?family=Cinzel:wght@500&family=Exo+2:wght@400;600&display=swap">
<style>
  :root {
    --stage: #e4e4e2;
    --paper: #ffffff;
    --paper-shade: #e9e9e9;
    --gold: #d9a21b;
    --gold-light: #e8bd45;
    --charcoal: #333333;
    --ink: #2b2b2b;
    --white: #ffffff;
  }
  * { margin: 0; padding: 0; box-sizing: border-box; }
  html, body { width: 1200px; height: 869px; overflow: hidden; }
  body { background: var(--stage); position: relative; font-family: "Exo 2", sans-serif; }

  .card {
    position: absolute;
    width: 680px;
    height: 390px;
    background: linear-gradient(135deg, var(--paper) 40%, var(--paper-shade));
    box-shadow: 0 6px 18px rgba(0,0,0,.18);
    overflow: hidden;
  }
  .card--front { left: 90px; top: 40px; }
  .card--back  { left: 430px; top: 440px; }

  /* front */
  .front-mark {
    position: absolute; left: 50%; top: 70px;
    width: 130px; height: 130px; margin-left: -65px;
    border-radius: 50%;
    background: radial-gradient(circle at 40% 35%, var(--gold-light), var(--gold));
  }
  .front-name {
    position: absolute; left: 0; right: 0; top: 236px;
    text-align: center;
    font-family: "Cinzel", serif; font-weight: 500;
    font-size: 30px; color: var(--ink);
  }

  /* back */
  .back-shapes { position: absolute; inset: 0; z-index: 0; }
  .back-mark {
    position: absolute; left: 30px; top: 22px;
    width: 88px; height: 88px; border-radius: 50%;
    background: radial-gradient(circle at 40% 35%, var(--gold-light), var(--gold));
    z-index: 1;
  }
  .back-name {
    position: absolute; left: 132px; top: 56px;
    font-family: "Cinzel", serif; font-weight: 500;
    font-size: 21px; color: var(--ink); z-index: 1;
  }
  .address {
    position: absolute; left: 96px; top: 151px;
    font-size: 15px; font-weight: 600; color: var(--white); letter-spacing: .3px;
    white-space: nowrap; z-index: 1;
  }
  .person { position: absolute; right: 36px; top: 100px; text-align: left; z-index: 2; white-space: nowrap; }
  .person__name { font-size: 27px; font-weight: 600; letter-spacing: 2px; color: var(--ink); line-height: 1; }
  .person__role { font-size: 11px; letter-spacing: 1.6px; color: var(--ink); margin-top: 5px; text-transform: uppercase; line-height: 1.2; }

  .contact { position: absolute; display: flex; align-items: center; gap: 12px; color: var(--white); font-size: 15px; letter-spacing: .4px; z-index: 1; white-space: nowrap; }
  .contact__icon { width: 26px; height: 26px; border-radius: 4px; background: var(--white); display: flex; align-items: center; justify-content: center; }
  .contact--web   { left: 52px; top: 192px; }
  .contact--mail  { left: 30px; top: 232px; }
  .contact--phone { left: 470px; top: 254px; }
  .contact--mobile{ left: 470px; top: 292px; }
</style>
</head>
<body>

<section class="card card--front">
  <div class="front-mark"></div>
  <p class="front-name">Mindtrainer Lou Varga</p>
</section>

<section class="card card--back">
  <svg class="back-shapes" width="680" height="390" viewBox="0 0 680 390">
    <defs>
      <linearGradient id="goldBand" x1="0" y1="0" x2="1" y2="0">
        <stop offset="0" stop-color="#d39a14"/>
        <stop offset=".45" stop-color="#e8bd45"/>
        <stop offset="1" stop-color="#d49c16"/>
      </linearGradient>
    </defs>
    <polygon points="0,176 394,176 430,216 680,216 680,334 0,334" fill="url(#goldBand)"/>
    <polygon points="22,146 400,146 440,200 680,200 680,216 430,216 394,176 0,176 0,160" fill="#333333"/>
    <rect x="0" y="334" width="680" height="56" fill="#333333"/>
  </svg>

  <div class="back-mark"></div>
  <p class="back-name">Mindtrainer Lou Varga</p>

  <p class="address">217,4th floor,Ridgeway Plaza Road TUC</p>

  <div class="person">
    <p class="person__name">MARA QUINLAN</p>
    <p class="person__role">General Manager</p>
  </div>

  <div class="contact contact--web">
    <span class="contact__icon">
      <svg width="18" height="18" viewBox="0 0 18 18" fill="none" stroke="#d9a21b" stroke-width="1.6">
        <circle cx="9" cy="9" r="7"/><ellipse cx="9" cy="9" rx="3" ry="7"/><line x1="2" y1="9" x2="16" y2="9"/>
      </svg>
    </span>
    <span>www.quellpractice.net</span>
  </div>
  <div class="contact contact--mail">
    <span class="contact__icon">
      <svg width="18" height="14" viewBox="0 0 18 14" fill="none" stroke="#d9a21b" stroke-width="1.6">
        <rect x="1" y="1" width="16" height="12"/><polyline points="1,1 9,8 17,1"/>
      </svg>
    </span>
    <span>lou@quellmail.net</span>
  </div>
  <div class="contact contact--phone">
    <span class="contact__icon">
      <svg width="16" height="16" viewBox="0 0 16 16">
        <path d="M4 1 L7 4 L5 6 Q7 10 10 11 L12 9 L15 12 L13 15 Q3 13 1 3 Z" fill="#d9a21b"/>
      </svg>
    </span>
    <span>520 555 0147</span>
  </div>
  <div class="contact contact--mobile">
    <span class="contact__icon">
      <svg width="12" height="18" viewBox="0 0 12 18">
        <rect x="1" y="1" width="10" height="16" rx="2" fill="#d9a21b"/>
        <rect x="3" y="3" width="6" height="10" fill="#ffffff"/>
      </svg>
    </span>
    <span>520 555 0193</span>
  </div>
</section>

</body>
</html>
```